Onlineshop für hochwertige Gebrauchtsättel für den Reitsport sucht Webdesign
Zielgruppe
Wir verkaufen hochwertige Gebrauchtsättel für den Reitsport und möchten Reiter jeder Altersgruppe ansprechen.
Aufgabenstellung
Farbgebung : grün braun (eventuell gelb), naturnahe Farben
Ein Logo ist bereits vorhanden.

```html
<!DOCTYPE html>
<html lang="de">
<head>
<meta charset="utf-8">
<title>Hedgerow Saddlery – Webdesign</title>
<link href="https://fonts.googleapis.com/css2?family=PT+Sans:wght@400;700&display=swap" rel="stylesheet">
<style>
:root{
  --green:#9ac31c;
  --brown:#6a4b1e;
  --ink:#3a2a14;
  --muted:#8a7a66;
  --page-bg:#f7f7f7;
  --white:#ffffff;
  --field:#eceff2;
}
*{box-sizing:border-box;margin:0;padding:0}
html,body{width:1135px;height:1200px;overflow:hidden;background:var(--white);font-family:"PT Sans",sans-serif;color:var(--brown)}
.canvas{position:relative;width:1135px;height:1200px}
.page{position:absolute;width:360px;height:460px;background:var(--page-bg);box-shadow:0 0 6px rgba(0,0,0,.18);overflow:hidden}
.page--home{left:138px;top:80px}
.page--saddles{left:642px;top:80px}
.page--prices{left:138px;top:649px}
.page--contact{left:642px;top:649px}

/* header */
.site-header{position:absolute;left:0;top:0;width:360px;height:31px;background:var(--white)}
.site-header__band{position:absolute;left:115px;top:0;width:130px;height:8px;background:var(--green);clip-path:polygon(0 0,100% 0,97% 100%,5% 100%)}
.site-header__mail{position:absolute;left:245px;top:4px;font-size:3.6px;color:var(--green);font-weight:700}
.brand{position:absolute;display:flex;flex-direction:column;align-items:center;color:var(--brown)}
.brand__dot{border-radius:50%;background:var(--green)}
.brand__name{font-weight:400;white-space:nowrap;letter-spacing:.02em}
.site-header .brand{left:70px;top:3px}
.site-header .brand__dot{width:14px;height:14px}
.site-header .brand__name{font-size:4.2px;margin-top:2px}
.nav{position:absolute;top:24px;left:0;font-size:3.6px;color:var(--ink)}
.nav span{position:absolute;white-space:nowrap}

/* footer */
.site-footer{position:absolute;left:0;top:410px;width:360px;height:50px;background:var(--white);text-align:center}
.site-footer .brand{left:50%;transform:translateX(-50%);top:7px}
.site-footer .brand__dot{width:9px;height:9px}
.site-footer .brand__name{font-size:2.8px;margin-top:1px}
.site-footer__line{position:absolute;left:0;width:100%;top:33px;font-size:4px;color:var(--ink)}
.site-footer__links{position:absolute;left:0;width:100%;top:40px;font-size:3px;color:var(--ink)}

.page-title{position:absolute;left:73px;top:46px;font-size:7px;font-weight:700;color:var(--green)}
.card{position:absolute;background:var(--white)}
.photo{position:absolute}

/* home */
.hero{position:absolute;left:0;top:31px;width:360px;height:127px;background:linear-gradient(100deg,#5b6b3a 0%,#a2491c 30%,#c0621f 60%,#7a5a3e 85%,#2f2a26 100%)}
.hero__title{position:absolute;left:0;width:370px;top:62px;text-align:center;color:var(--white);font-size:7px;font-weight:700}
.hero__sub{position:absolute;left:0;width:370px;top:71px;text-align:center;color:var(--white);font-size:6px}
.intro-card{left:70px;top:165px;width:220px;height:239px}
.intro-card .brand{left:50%;transform:translateX(-50%);top:13px}
.intro-card .brand__dot{width:22px;height:22px}
.intro-card .brand__name{font-size:5px;margin-top:2px}
.feature__img{position:absolute;left:45px;width:55px;height:36px}
.feature__text{position:absolute;left:110px;width:72px;font-size:3px;line-height:4.9px;color:var(--brown)}
.feature__text b{display:block;font-size:3.4px;color:var(--ink)}

/* saddles */
.saddle-card{left:70px;top:59px;width:220px;height:343px}
.saddle{position:absolute;width:60px;font-size:3px;line-height:4.9px;color:var(--brown)}
.saddle__img{width:52px;height:52px;background:radial-gradient(circle at 55% 45%,#2a2420 0%,#3e332c 35%,#cfcfcf 70%,#f2f2f2 100%);margin-bottom:7px}
.saddle b{display:block;font-size:3.4px;color:var(--ink)}
.saddle u{display:block}

/* prices */
.price-card{left:70px;top:58px;width:220px;height:343px}
.price-card .brand{left:116px;top:9px;transform:translateX(-50%)}
.price-card .brand__dot{width:32px;height:32px}
.price-card .brand__name{font-size:7.5px;margin-top:3px}
.block-head{position:absolute;font-size:3.6px;font-weight:700;color:var(--ink)}
.price-list{position:absolute;width:45px;font-size:3px;line-height:4.9px;color:var(--brown)}
.price-list p{display:flex;justify-content:space-between}
.price-copy{position:absolute;top:256px;width:100px;font-size:4px;line-height:5.6px;color:var(--brown)}

/* contact */
.contact-card{left:70px;top:64px;width:220px;height:342px}
.contact-lead{position:absolute;left:3px;top:6px;font-size:3.4px;font-weight:700;color:var(--ink)}
.field{position:absolute;left:3px;width:100px;height:10px;background:var(--field);font-size:3.2px;color:var(--muted);padding:3px 3px}
.field--message{width:211px;height:75px;top:64px}
.address{position:absolute;left:119px;top:18px;font-size:3.6px;line-height:5.6px;color:var(--brown)}
.check{position:absolute;left:3px;font-size:3.2px;color:var(--muted);display:flex;align-items:center;gap:4px}
.check i{display:block;width:5px;height:5px;border:0.5px solid #cfd3d6}
.send{position:absolute;left:90px;top:168px;width:42px;height:11px;background:var(--green);color:var(--white);font-size:5.6px;font-weight:700;text-align:center;line-height:11px}
.map{position:absolute;left:6px;top:204px;width:209px;height:131px;background:linear-gradient(135deg,#e9ecea 0%,#dfe9d6 45%,#eef0ec 100%)}
</style>
</head>
<body>
<main class="canvas">

  <!-- Startseite -->
  <section class="page page--home">
    <header class="site-header">
      <div class="site-header__band"></div>
      <span class="site-header__mail">marla@hedgerowsattel.de</span>
      <div class="brand"><span class="brand__dot"></span><span class="brand__name">HEDGEROW SADDLERY</span></div>
      <nav class="nav"><span style="left:188px">Home</span><span style="left:217px">Sättel</span><span style="left:246px">Preise</span><span style="left:276px">Kontakt</span></nav>
    </header>
    <div class="hero" role="img" aria-label="Reiterin auf einem Fuchs mit Sattel neben einem braunen Pferd auf dem Turnierplatz"></div>
    <p class="hero__title">Gebrauchte Markensättel</p>
    <p class="hero__sub">in allerbester Qualität</p>
    <div class="card intro-card">
      <div class="brand"><span class="brand__dot"></span><span class="brand__name">HEDGEROW SADDLERY</span></div>
      <div class="photo feature__img" style="top:71px;background:linear-gradient(135deg,#5f7a46,#3c2a22 55%,#7f9a5c)" role="img" aria-label="Springsattel auf einem Holzzaun"></div>
      <p class="feature__text" style="top:71px">Du suchst einen hochwertigen Gebrauchtsattel? Dann bist du genau richtig bei uns. Wir haben immer 100-150 gebrauchte Sättel aller Marken und Preisklassen im Angebot. Außerdem bieten wir den Ankauf sowie Kommissionsverkauf von gebrauchten Sätteln an.</p>
      <div class="photo feature__img" style="top:123px;background:#eeeeee;border:0.5px solid #cccccc" role="img" aria-label="Platzhalter für ein Teamfoto"></div>
      <p class="feature__text" style="top:123px"><b>Das Hedgerow-Team</b>Wir sind ein kleines Team aus Reitern, die Sättel lieben. Wir beraten dich ehrlich, prüfen jeden Sattel sorgfältig und helfen dir, den passenden für dein Pferd zu finden.</p>
      <div class="photo feature__img" style="top:174px;background:linear-gradient(135deg,#8a5a35,#2a2320 50%,#b48b6c)" role="img" aria-label="Dressursattel mit Schabracke auf einem braunen Pferd"></div>
      <p class="feature__text" style="top:174px"><b>Sattelanprobe</b>Gerne kommen wir mit einer Auswahl passender Sättel zu dir in den Stall und probieren sie direkt an deinem Pferd aus, damit Reiter und Pferd sich wohlfühlen.</p>
    </div>
    <footer class="site-footer">
      <div class="brand"><span class="brand__dot"></span><span class="brand__name">HEDGEROW SADDLERY</span></div>
      <p class="site-footer__line">Hedgerow Saddlery | Marla Osten | Lindenhof 4 | 64999 Talbrunn | marla@hedgerowsattel.de</p>
      <p class="site-footer__links">Kontakt | Impressum | Datenschutzerklärung | Widerrufsbelehrung</p>
    </footer>
  </section>

  <!-- Sattelauswahl -->
  <section class="page page--saddles">
    <header class="site-header">
      <div class="site-header__band"></div>
      <span class="site-header__mail">marla@hedgerowsattel.de</span>
      <div class="brand"><span class="brand__dot"></span><span class="brand__name">HEDGEROW SADDLERY</span></div>
      <nav class="nav"><span style="left:188px">Home</span><span style="left:217px">Sättel</span><span style="left:246px">Preise</span><span style="left:276px">Kontakt</span></nav>
    </header>
    <h1 class="page-title">Sattelauswahl</h1>
    <div class="card saddle-card"></div>
    <div class="saddle" style="left:76px;top:64px"><div class="saddle__img" role="img" aria-label="Schwarzer Dressursattel"></div><b>Satteltyp &amp; Marke</b>Sitzfläche: XX Zoll<br>Sattelblatt: normal<br>Kammerweite: XXX<br>Baujahr: XXXX<br>Farbe: XXXXX<u>mehr erfahren</u></div>
    <div class="saddle" style="left:155px;top:64px"><div class="saddle__img" role="img" aria-label="Brauner Dressursattel"></div><b>Satteltyp &amp; Marke</b>Sitzfläche: XX Zoll<br>Sattelblatt: normal<br>Kammerweite: XXX<br>Baujahr: XXXX<br>Farbe: XXXXX<u>mehr erfahren</u></div>
    <div class="saddle" style="left:233px;top:64px"><div class="saddle__img" role="img" aria-label="Schwarzer Dressursattel"></div><b>Satteltyp &amp; Marke</b>Sitzfläche: XX Zoll<br>Sattelblatt: normal<br>Kammerweite: XXX<br>Baujahr: XXXX<br>Farbe: XXXXX<u>mehr erfahren</u></div>
    <div class="saddle" style="left:76px;top:179px"><div class="saddle__img" role="img" aria-label="Schwarzer Dressursattel"></div><b>Satteltyp &amp; Marke</b>Sitzfläche: XX Zoll<br>Sattelblatt: normal<br>Kammerweite: XXX<br>Baujahr: XXXX<br>Farbe: XXXXX<u>mehr erfahren</u></div>
    <div class="saddle" style="left:155px;top:179px"><div class="saddle__img" role="img" aria-label="Brauner Dressursattel"></div><b>Satteltyp &amp; Marke</b>Sitzfläche: XX Zoll<br>Sattelblatt: normal<br>Kammerweite: XXX<br>Baujahr: XXXX<br>Farbe: XXXXX<u>mehr erfahren</u></div>
    <div class="saddle" style="left:233px;top:179px"><div class="saddle__img" role="img" aria-label="Schwarzer Dressursattel"></div><b>Satteltyp &amp; Marke</b>Sitzfläche: XX Zoll<br>Sattelblatt: normal<br>Kammerweite: XXX<br>Baujahr: XXXX<br>Farbe: XXXXX<u>mehr erfahren</u></div>
    <div class="saddle" style="left:76px;top:299px"><div class="saddle__img" role="img" aria-label="Schwarzer Dressursattel"></div><b>Satteltyp &amp; Marke</b>Sitzfläche: XX Zoll<br>Sattelblatt: normal<br>Kammerweite: XXX<br>Baujahr: XXXX<br>Farbe: XXXXX<u>mehr erfahren</u></div>
    <div class="saddle" style="left:155px;top:299px"><div class="saddle__img" role="img" aria-label="Brauner Dressursattel"></div><b>Satteltyp &amp; Marke</b>Sitzfläche: XX Zoll<br>Sattelblatt: normal<br>Kammerweite: XXX<br>Baujahr: XXXX<br>Farbe: XXXXX<u>mehr erfahren</u></div>
    <div class="saddle" style="left:233px;top:299px"><div class="saddle__img" role="img" aria-label="Schwarzer Dressursattel"></div><b>Satteltyp &amp; Marke</b>Sitzfläche: XX Zoll<br>Sattelblatt: normal<br>Kammerweite: XXX<br>Baujahr: XXXX<br>Farbe: XXXXX<u>mehr erfahren</u></div>
    <footer class="site-footer">
      <div class="brand"><span class="brand__dot"></span><span class="brand__name">HEDGEROW SADDLERY</span></div>
      <p class="site-footer__line">Hedgerow Saddlery | Marla Osten | Lindenhof 4 | 64999 Talbrunn | marla@hedgerowsattel.de</p>
      <p class="site-footer__links">Kontakt | Impressum | Datenschutzerklärung | Widerrufsbelehrung</p>
    </footer>
  </section>

  <!-- Preisliste -->
  <section class="page page--prices">
    <header class="site-header">
      <div class="site-header__band"></div>
      <span class="site-header__mail">marla@hedgerowsattel.de</span>
      <div class="brand"><span class="brand__dot"></span><span class="brand__name">HEDGEROW SADDLERY</span></div>
      <nav class="nav"><span style="left:188px">Home</span><span style="left:217px">Sättel</span><span style="left:246px">Preise</span><span style="left:276px">Kontakt</span></nav>
    </header>
    <h1 class="page-title">Preisliste</h1>
    <div class="card price-card">
      <div class="brand"><span class="brand__dot"></span><span class="brand__name">HEDGEROW SADDLERY</span></div>
      <p class="block-head" style="left:7px;top:13px">Sattelanprobe</p>
      <div class="price-list" style="left:7px;top:23px;width:38px"><p><span>Je Stunde:</span><span>XXX €</span></p><p><span>Anfahrt je km:</span><span>XXX €</span></p><br><p><span>Sattelcheck:</span><span>XXX €</span></p><p><span>Polsterung:</span><span>XXX €</span></p></div>
      <p class="block-head" style="left:7px;top:75px">Sattelpreise</p>
      <div class="price-list" style="left:7px;top:85px"><p><span>Dressur 16"</span><span>XXX €</span></p><p><span>Dressur 17"</span><span>XXX €</span></p><p><span>Dressur 18"</span><span>XXX €</span></p><p><span>Springen 16"</span><span>XXX €</span></p><p><span>Springen 17"</span><span>XXX €</span></p><p><span>Springen 18"</span><span>XXX €</span></p><p><span>VS-Sattel 16"</span><span>XXX €</span></p><p><span>VS-Sattel 17"</span><span>XXX €</span></p><p><span>VS-Sattel 18"</span><span>XXX €</span></p><p><span>Kinder 15"</span><span>XXX €</span></p><p><span>Pony 15,5"</span><span>XXX €</span></p><p><span>Wanderreiten</span><span>XXX €</span></p></div>
      <div class="price-list" style="left:84px;top:85px"><p><span>Lederpflege</span><span>XXX €</span></p><p><span>Gurt kurz</span><span>XXX €</span></p><p><span>Gurt lang</span><span>XXX €</span></p><p><span>Steigbügel</span><span>XXX €</span></p><p><span>Bügelriemen</span><span>XXX €</span></p><p><span>Schabracke</span><span>XXX €</span></p><p><span>Lammfell</span><span>XXX €</span></p><p><span>Pad Gel</span><span>XXX €</span></p><p><span>Sattelschoner</span><span>XXX €</span></p><p><span>Sattelhalter</span><span>XXX €</span></p><p><span>Vorderzeug</span><span>XXX €</span></p><p><span>Sattelbezug</span><span>XXX €</span></p></div>
      <div class="price-list" style="left:161px;top:85px"><p><span>Kopfeisen S</span><span>XXX €</span></p><p><span>Kopfeisen M</span><span>XXX €</span></p><p><span>Kopfeisen W</span><span>XXX €</span></p><p><span>Umpolstern</span><span>XXX €</span></p><p><span>Nachpolstern</span><span>XXX €</span></p><p><span>Nähte</span><span>XXX €</span></p><p><span>Pauschen</span><span>XXX €</span></p><p><span>Strippen</span><span>XXX €</span></p><p><span>Kissen neu</span><span>XXX €</span></p><p><span>Sitz neu</span><span>XXX €</span></p><p><span>Versand</span><span>XXX €</span></p><p><span>Abholung</span><span>XXX €</span></p></div>
      <div class="price-list" style="left:7px;top:162px"><p><span>Ankauf klein</span><span>XXX €</span></p><p><span>Ankauf groß</span><span>XXX €</span></p><p><span>Kommission</span><span>XXX €</span></p><p><span>Bewertung</span><span>XXX €</span></p><p><span>Fotoservice</span><span>XXX €</span></p><p><span>Inserat</span><span>XXX €</span></p><p><span>Testwoche</span><span>XXX €</span></p><p><span>Testtag</span><span>XXX €</span></p><p><span>Kaution</span><span>XXX €</span></p><p><span>Rücknahme</span><span>XXX €</span></p><p><span>Tausch</span><span>XXX €</span></p><p><span>Lagerung</span><span>XXX €</span></p></div>
      <div class="photo" style="left:84px;top:158px;width:120px;height:80px;background:linear-gradient(120deg,#6d8a4a 0%,#7b4a26 40%,#5a3320 65%,#8fa069 100%)" role="img" aria-label="Braunes Pferd mit Dressursattel vor einem Stall"></div>
      <p class="price-copy" style="left:7px">Alle Preise verstehen sich inklusive Mehrwertsteuer. Jeder Sattel wird vor dem Verkauf von uns geprüft, gereinigt und gepflegt. Auf Wunsch passen wir die Polsterung an dein Pferd an. Bei Fragen zu einzelnen Modellen oder zur passenden Kammerweite melde dich gerne jederzeit bei uns. Wir nehmen uns Zeit für dich und dein Pferd.</p>
      <p class="price-copy" style="left:110px">Die Anfahrt zur Sattelanprobe berechnen wir ab unserem Hof. Wird ein Sattel gekauft, entfallen die Kosten der Anprobe. Ankauf und Kommission erfolgen nach Besichtigung. Wir bewerten deinen Sattel fair und transparent und kümmern uns um Fotos, Inserat und Abwicklung, damit du dich entspannt zurücklehnen kannst.</p>
    </div>
    <footer class="site-footer">
      <div class="brand"><span class="brand__dot"></span><span class="brand__name">HEDGEROW SADDLERY</span></div>
      <p class="site-footer__line">Hedgerow Saddlery | Marla Osten | Lindenhof 4 | 64999 Talbrunn | marla@hedgerowsattel.de</p>
      <p class="site-footer__links">Kontakt | Impressum | Datenschutzerklärung | Widerrufsbelehrung</p>
    </footer>
  </section>

  <!-- Kontakt -->
  <section class="page page--contact">
    <header class="site-header">
      <div class="site-header__band"></div>
      <span class="site-header__mail">marla@hedgerowsattel.de</span>
      <div class="brand"><span class="brand__dot"></span><span class="brand__name">HEDGEROW SADDLERY</span></div>
      <nav class="nav"><span style="left:188px">Home</span><span style="left:217px">Sättel</span><span style="left:246px">Preise</span><span style="left:276px">Kontakt</span></nav>
    </header>
    <h1 class="page-title">Kontakt</h1>
    <div class="card contact-card">
      <p class="contact-lead">Du hast weitere Fragen? Dann stell Sie uns gerne hier im Kontaktformular</p>
      <div class="field" style="top:18px">Name</div>
      <div class="field" style="top:33px">Email Adresse</div>
      <div class="field" style="top:49px">Betreff</div>
      <p class="address">Hedgerow Saddlery<br>Marla Osten<br>Lindenhof 4<br>64999 Talbrunn<br><span style="display:block;height:3px"></span>0151 48203917<br>marla@hedgerowsattel.de</p>
      <div class="field field--message">Nachricht</div>
      <p class="check" style="top:146px"><i></i>Kopie an mich senden</p>
      <p class="check" style="top:156px"><i></i>Hiermit bestätige ich, dass ich die Datenschutzerklärung gelesen habe und ihr zustimme</p>
      <div class="send">Absenden</div>
      <div class="map" role="img" aria-label="Straßenkarte der Umgebung mit Standortmarkierungen"></div>
    </div>
    <footer class="site-footer">
      <div class="brand"><span class="brand__dot"></span><span class="brand__name">HEDGEROW SADDLERY</span></div>
      <p class="site-footer__line">Hedgerow Saddlery | Marla Osten | Lindenhof 4 | 64999 Talbrunn | marla@hedgerowsattel.de</p>
      <p class="site-footer__links">Kontakt | Impressum | Datenschutzerklärung | Widerrufsbelehrung</p>
    </footer>
  </section>

</main>
</body>
</html>
```